Outgrow the Corner Office Author needs smart sample illustration for book

Business author in need of illustrations for a business book. Establish an illustration style based on rough sketch provided for a book called, "Outgrow the Corner Office." If this sample works well, there are 15 more illustrations needed. Process: 1) Use sketch provided as a basis for stylizing an illustration that is: polished, potentially whimsical, simple, appropriate for a serious career topic, black & white line art only. No thick markers like those use in graphic recordings, rather something using a fendra or thin black quillex marker 2) Follow concept / sketch closely. I am not looking for broad interpretations of concept, rather a refinement of the rough sketch. 3) Want to own final illustration - Will consider sharing a headline on the book (published in March 2017) if illustrator is chosen for the complete set of illustrations. 4) Require hand lettering as that is part of the illustration
Updates

I am looking for hand-drawn illustration, rather than computer-generated images. Hand-lettering is important. Simple hand-lettering.

Target Market(s)

Agile thinkers, entrepreneurs, employees who want more creativity, growth, and happiness in their careers. They want to figure out the future of work and how to embrace change

Industry/Entity Type

Business

Other font styles liked:
• Hand lettering, simple , Like all Caps printing, but will consider U & LC

Requirements
Must have
• Process: 1) Use sketch provided as a basis for stylizing an illustration that is: polished, potentially whimsical, simple, appropriate for a serious career topic, black & white line art only. No thick markers like those use in graphic recordings, rather something using a fendra or thin black quillex marker 2) Follow concept / sketch closely. I am not looking for broad interpretations of concept, rather a refinement of the rough sketch. 3) Want to own final illustration - Will consider sharing a headline on the book (published in March 2017) if illustrator is chosen for the complete set of illustrations. 4) Require hand lettering as that is part of the illustration
Should not have
• no thick markers used in sketches
• No water color, or ink wash or gray scale (MUST be high contrast black & white lines only)
• DO NOT Illustrate the Ladder Compass Mapping Model Illustration, rather, use it for reference. If I find a relevant illustrator, this model will be one of the illustrations to be completed in the appropriate style.

```html
<!DOCTYPE html>
<html lang="en">
<head>
<meta charset="utf-8">
<title>Career Journey Path</title>
<link rel="stylesheet" href="https://fonts.googleapis.com/css2?family=Caveat:wght@600&display=swap">
<style>
  :root {
    --paper: #ffffff;
    --ink: #111111;
    --figure-tone: #e6e6e6;
  }
  html, body {
    margin: 0;
    padding: 0;
    overflow: hidden;
    background: var(--paper);
  }
  .canvas {
    position: relative;
    width: 1200px;
    height: 862px;
    background: var(--paper);
    overflow: hidden;
  }
  .cyclist {
    position: absolute;
    left: 66px;
    top: 300px;
    width: 216px;
    height: 234px;
    background: var(--figure-tone);
    border-radius: 40px 40px 110px 110px;
  }
  .journey {
    position: absolute;
    inset: 0;
    width: 1200px;
    height: 862px;
  }
  .journey-line {
    fill: none;
    stroke: var(--ink);
    stroke-width: 3;
    stroke-linecap: round;
  }
  .milestone {
    fill: var(--ink);
  }
  .stage-label {
    font-family: "Caveat", cursive;
    font-weight: 600;
    font-size: 34px;
    fill: var(--ink);
  }
</style>
</head>
<body>
  <main class="canvas">
    <div class="cyclist" role="img" aria-label="Line drawing of a cyclist in a helmet riding a bicycle toward the path"></div>

    <svg class="journey" viewBox="0 0 1200 862" aria-label="Five-stage career journey path">
      <path class="journey-line"
        d="M296,459 C320,440 350,420 400,405 C450,392 520,400 560,420 C620,450 650,430 677,409 C720,375 770,345 816,341 C900,335 980,360 1033,341 C1045,335 1052,315 1056,300"/>

      <circle class="milestone" cx="334" cy="429" r="8"/>
      <circle class="milestone" cx="502" cy="404" r="8"/>
      <circle class="milestone" cx="677" cy="409" r="8"/>
      <circle class="milestone" cx="816" cy="341" r="8"/>
      <circle class="milestone" cx="1033" cy="341" r="8"/>

      <text class="stage-label" x="326" y="476">1.Discover</text>
      <text class="stage-label" x="508" y="400">2.Define</text>
      <text class="stage-label" x="680" y="450">3.Design</text>
      <text class="stage-label" x="810" y="325">4.Deliver</text>
      <text class="stage-label" x="982" y="412">5.Develope</text>
    </svg>
  </main>
</body>
</html>
```